Powerpoint for consulting dentalpractices on management, improvement, and benchmarks

Fase 1: create 8-15 slides to be used for the model. The are the basic slideexamples for future presentation.
colour scheme and font types as in attachment for older powerpoint. Fonts, logo and colourscheme stay the same. Newer slidedeck contains newer ideas for new presentations. Smaller logo maybe better to be used for all slides. Normal logo for starting and end slide. Open for your inspiration and new suggestions
Fase 2 create slidemaster to enable us to create new slidedesks faster.

Target Market(s)

Dentalpractices (no dental images in powerpoint)

Industry/Entity Type

Dental practices

Font styles to use
Other font styles liked:
• Roobert for heading Normal Text Inter

Requirements
Must have
• Different slidemaster basic slides to quickly create slides with full slide pictures which still have a Molvaro touch. Content slides, slides with bullets and slides to show 3 -5 subjects
Nice to have
• New styling element for recognition of brand
Should not have
• round edges, complex slide master

```html
<!DOCTYPE html>
<html lang="nl">
<head>
<meta charset="utf-8">
<title>Molvaro – Taakdelegatie slide deck</title>
<link href="https://fonts.googleapis.com/css2?family=Inter:wght@300;400;600;700&family=Rubik:wght@500;600;700&display=swap" rel="stylesheet">
<style>
:root{
  --blue:#1b57a3;
  --blue-dark:#123f7a;
  --green:#74bb1f;
  --red:#e1262d;
  --grey:#5c5c5c;
  --text:#1f1f1f;
  --muted:#8a8a8a;
  --canvas:#9d9d9d;
  --white:#ffffff;
}
*{box-sizing:border-box;margin:0;padding:0}
html,body{width:894px;height:1200px;overflow:hidden}
body{background:var(--canvas);font-family:"Inter",sans-serif;color:var(--text);position:relative}
.slide{position:absolute;width:529px;height:297px;background:var(--white);overflow:hidden;transform:scale(.541);transform-origin:0 0;box-shadow:0 2px 6px rgba(0,0,0,.25)}
.slide.cover{width:832px;height:467px}
.strip{position:absolute;left:0;top:0;width:100%;height:5px;background:linear-gradient(90deg,var(--blue),var(--green))}
.s-title{position:absolute;left:23px;top:22px;font-family:"Rubik",sans-serif;font-weight:600;font-size:20px;color:var(--blue)}
.foot{position:absolute;left:0;bottom:0;width:100%;height:30px}
.pg{position:absolute;left:23px;top:9px;font-size:10px;color:var(--blue)}
.copy{position:absolute;left:212px;top:12px;font-size:5px;color:var(--muted);letter-spacing:.2px}
.brand{position:absolute;right:23px;top:5px;font-family:"Rubik",sans-serif;font-weight:500;font-size:14px;color:var(--blue)}
.photo{position:absolute}
ul.bul{list-style:none;font-size:8.3px;line-height:1.3}
ul.bul li{position:relative;padding-left:9px;margin-bottom:3px}
ul.bul li::before{content:"•";position:absolute;left:0}
ul.bul li.hl-blue{color:var(--blue);font-weight:600}
ul.bul li.hl-green{color:var(--green);font-weight:600}
ul.tight{font-size:7.2px;line-height:1.35}
ul.tight li{margin-bottom:0}
.lead{font-weight:700;color:var(--green);font-size:11.5px;line-height:1.05}
.bar{position:absolute;height:20px;color:var(--white);font-family:"Rubik",sans-serif;font-weight:600;font-size:9px;padding:5px 8px;letter-spacing:.3px}
.bar.blue{background:var(--blue)}
.bar.green{background:var(--green)}
.abs{position:absolute}

/* cover */
.cover-title{position:absolute;left:0;top:232px;width:476px;height:135px;background:rgba(27,87,163,.9);padding:16px 32px;font-family:"Rubik",sans-serif;font-weight:700;font-size:47px;line-height:1.08;color:var(--white)}
.cover-sub{position:absolute;left:0;top:367px;width:476px;height:55px;background:var(--green);padding:15px 32px;font-weight:300;font-size:19px;color:var(--white)}
.cover-foot{position:absolute;left:0;top:422px;width:100%;height:45px;background:var(--white);padding:18px 30px;font-size:8.5px;color:var(--muted)}
.cover-brand{position:absolute;left:678px;top:40px;font-family:"Rubik",sans-serif;font-weight:500;font-size:32px;color:var(--blue)}

/* agenda */
.agenda-title{position:absolute;left:154px;top:22px;font-family:"Rubik",sans-serif;font-weight:600;font-size:19px;color:var(--blue)}
.agenda-title span{color:var(--green)}
.ag{position:absolute;display:flex;align-items:center;gap:7px;font-size:9.5px;color:var(--blue);line-height:1.1;width:180px}
.ag b{flex:none;width:40px;height:40px;border-radius:50%;color:var(--white);font-family:"Rubik",sans-serif;font-weight:600;font-size:17px;display:flex;align-items:center;justify-content:center}
.c-blue{background:var(--blue)}.c-green{background:var(--green)}.c-grey{background:var(--grey)}.c-red{background:var(--red)}

.hero-title{position:absolute;left:265px;font-family:"Rubik",sans-serif;font-weight:600;color:var(--white)}
.hero-text{position:absolute;left:265px;font-size:8.5px;line-height:1.25;color:var(--white);width:245px}

.col3{position:absolute;top:125px;width:150px;text-align:center;font-size:7.2px;line-height:1.3}

table.inr{position:absolute;left:265px;top:103px;width:242px;border-collapse:collapse;font-size:7.5px}
table.inr th{background:var(--blue);color:var(--white);font-weight:600;padding:4px 8px;text-align:left}
table.inr th+th{text-align:center}
table.inr td{padding:3.5px 8px;border-bottom:1px solid #fff}
table.inr td+td{text-align:center}
table.inr tr:nth-child(odd) td{background:#eeeeee}
table.inr tr.norm td{outline:1px dashed var(--green)}
.inr-note{position:absolute;left:265px;top:247px;width:242px;height:12px;background:var(--green);color:var(--white);font-size:6.5px;text-align:center;padding-top:2px}

.pin-lbl{position:absolute;top:150px;width:100px;text-align:center;font-family:"Rubik",sans-serif;font-weight:600;font-size:9px;line-height:1.2}
.pin-lbl small{display:block;font-family:"Inter",sans-serif;font-weight:400;font-size:6.5px;margin-top:2px}
.t-blue{color:var(--blue)}.t-green{color:var(--green)}.t-red{color:var(--red)}
</style>
</head>
<body>

<!-- Cover -->
<section class="slide cover" style="left:87px;top:50px">
  <div class="photo" role="img" aria-label="Foto: tandarts behandelt een patiënte" style="left:0;top:0;width:832px;height:467px;background:linear-gradient(120deg,#d9d6d2 0%,#c7c9cc 40%,#8fb0dc 70%,#3a74c9 100%)"></div>
  <svg class="abs" style="left:0;top:0" width="832" height="467" viewBox="0 0 832 467"><path d="M420 0 H832 V467 H800 C790 250 650 80 420 0Z" fill="#ffffff"/></svg>
  <div class="cover-brand">Molvaro</div>
  <div class="cover-title">Taakdelegatie<br>en de controle</div>
  <div class="cover-sub">Tandartspraktijk Verhoeven</div>
  <div class="cover-foot">©2023 MOLVARO <span style="color:var(--green)">|</span> ALL RIGHTS RESERVED</div>
</section>

<!-- Agenda -->
<section class="slide" style="left:593px;top:193px">
  <div class="strip"></div>
  <div class="photo" role="img" aria-label="Foto: lachende patiënt in de stoel" style="left:0;top:5px;width:138px;height:292px;background:linear-gradient(160deg,#c9d3dc,#7f9ab8 60%,#3d6ea8)"></div>
  <div class="agenda-title">Agenda <span>Taakdelegatie</span></div>
  <div class="ag" style="left:154px;top:72px"><b class="c-blue">01</b>Risicofactoren</div>
  <div class="ag" style="left:154px;top:117px"><b class="c-green">02</b>Gevolgen van de<br>risicofactoren</div>
  <div class="ag" style="left:154px;top:164px"><b class="c-grey">03</b>Medische anamnese</div>
  <div class="ag" style="left:154px;top:210px"><b class="c-red">04</b>INR waarde</div>
  <div class="ag" style="left:333px;top:72px"><b class="c-red">05</b>Veelvoorkomende<br>medicatie en ziekte</div>
  <div class="ag" style="left:333px;top:117px"><b class="c-grey">06</b>Dossiervoering</div>
  <div class="ag" style="left:333px;top:164px"><b class="c-green">07</b>Enkele handige zinnen</div>
  <div class="ag" style="left:333px;top:210px"><b class="c-blue">08</b>Appendix</div>
  <div class="foot"><span class="copy" style="left:212px">©2023 MOLVARO | ALL RIGHTS RESERVED</span><span class="brand">Molvaro</span></div>
</section>

<!-- 3 bullets -->
<section class="slide" style="left:15px;top:360px">
  <div class="strip"></div>
  <div class="s-title">Slide title</div>
  <ul class="bul abs" style="left:23px;top:64px;width:485px">
    <li>Lorem ipsum dolor sit amet, consectetuer adipiscing elit. Maecenas porttitor congue massa. Fusce posuere, magna sed pulvinar ultricies, purus lectus malesuada libero, sit amet commodo magna eros quis urna.</li>
    <li class="hl-blue">Nunc viverra imperdiet enim. Fusce est. Vivamus a tellus.</li>
    <li>Pellentesque habitant morbi tristique senectus et netus et malesuada fames ac turpis egestas. Proin pharetra nonummy pede. Mauris et orci.</li>
    <li>Lorem ipsum dolor sit amet, consectetuer adipiscing elit. Maecenas porttitor congue massa. Fusce posuere, magna sed pulvinar ultricies, purus lectus malesuada libero, sit amet commodo magna eros quis urna.</li>
    <li class="hl-green">Nunc viverra imperdiet enim. Fusce est. Vivamus a tellus.</li>
    <li>Pellentesque habitant morbi tristique senectus et netus et malesuada fames ac turpis egestas. Proin pharetra nonummy pede. Mauris et orci.</li>
    <li>Lorem ipsum dolor sit amet, consectetuer adipiscing elit. Maecenas porttitor congue massa. Fusce posuere, magna sed pulvinar ultricies, purus lectus malesuada libero, sit amet commodo magna eros quis urna.</li>
  </ul>
  <div class="foot"><span class="pg">3</span><span class="copy">©2023 MOLVARO | ALL RIGHTS RESERVED</span><span class="brand">Molvaro</span></div>
</section>

<!-- 4 full photo -->
<section class="slide" style="left:304px;top:360px">
  <div class="photo" role="img" aria-label="Foto: behandeling in de stoel, donker getint" style="left:0;top:0;width:529px;height:297px;background:linear-gradient(120deg,#6f7378,#4f555d 45%,#3d4f63 75%,#2d4c6e)"></div>
  <div class="abs" style="left:265px;top:148px;width:50px;height:4px;background:var(--green)"></div>
  <div class="hero-title" style="top:170px;font-size:23px">Slide title</div>
  <div class="hero-text" style="top:200px">Lorem ipsum dolor sit amet, consectetuer adipiscing elit. Maecenas porttitor congue massa.</div>
</section>

<!-- 5 lead + bullets -->
<section class="slide" style="left:593px;top:360px">
  <div class="strip"></div>
  <div class="s-title">Slide title</div>
  <p class="lead abs" style="left:23px;top:64px;width:470px">Lorem ipsum dolor sit amet, consectetuer adipiscing elit. Maecenas porttitor congue massa. Fusce posuere, magna sed pulvinar ultricies, purus lectus malesuada libero, sit amet commodo magna eros quis urna.</p>
  <ul class="bul abs" style="left:23px;top:117px;width:485px">
    <li>Lorem ipsum dolor sit amet, consectetuer adipiscing elit. Maecenas porttitor congue massa. Fusce posuere, magna sed pulvinar ultricies, purus lectus malesuada libero, sit amet commodo magna eros quis urna.</li>
    <li class="hl-blue">Nunc viverra imperdiet enim. Fusce est. Vivamus a tellus.</li>
    <li>Pellentesque habitant morbi tristique senectus et netus et malesuada fames ac turpis egestas. Proin pharetra nonummy pede. Mauris et orci.</li>
  </ul>
  <div class="foot"><span class="pg">5</span><span class="copy">©2023 MOLVARO | ALL RIGHTS RESERVED</span><span class="brand">Molvaro</span></div>
</section>

<!-- 6 text + photo right -->
<section class="slide" style="left:15px;top:528px">
  <div class="strip"></div>
  <div class="s-title">Slide title</div>
  <div class="photo" role="img" aria-label="Foto: stralende glimlach" style="left:262px;top:0;width:267px;height:267px;background:linear-gradient(100deg,#dbeaf5,#f3ece6 45%,#e8c9b8 80%,#d9b7a5)"></div>
  <p class="lead abs" style="left:23px;top:64px;width:220px">Lorem ipsum dolor sit amet, consectetuer adipiscing elit.</p>
  <ul class="bul abs" style="left:23px;top:94px;width:225px">
    <li>Lorem ipsum dolor sit amet, consectetuer adipiscing elit. Maecenas porttitor congue massa. Fusce posuere, magna sed pulvinar ultricies, purus lectus malesuada libero, sit amet commodo magna eros quis urna.</li>
    <li>Nunc viverra imperdiet enim. Fusce est. Vivamus a tellus.</li>
    <li>Pellentesque habitant morbi tristique senectus et netus et malesuada fames ac turpis egestas. Proin pharetra nonummy pede. Mauris et orci.</li>
  </ul>
  <div class="foot"><span class="pg">6</span><span class="copy">©2023 MOLVARO | ALL RIGHTS RESERVED</span><span class="brand">Molvaro</span></div>
</section>

<!-- 7 three columns with images -->
<section class="slide" style="left:304px;top:528px">
  <div class="strip"></div>
  <div class="s-title">Slide title</div>
  <div class="abs" style="left:23px;top:59px;width:30px;height:5px;background:var(--blue)"></div>
  <div class="abs" style="left:189px;top:59px;width:30px;height:5px;background:var(--green)"></div>
  <div class="abs" style="left:355px;top:59px;width:30px;height:5px;background:var(--red)"></div>
  <div class="photo" role="img" aria-label="Foto: team in een behandelkamer" style="left:23px;top:64px;width:150px;height:84px;background:linear-gradient(135deg,#d6e4ef,#9fb8cf)"></div>
  <div class="photo" role="img" aria-label="Foto: medewerkers in de praktijk" style="left:189px;top:64px;width:150px;height:84px;background:linear-gradient(135deg,#e4e2de,#a9a59e)"></div>
  <div class="photo" role="img" aria-label="Foto: medewerker met een model" style="left:355px;top:64px;width:150px;height:84px;background:linear-gradient(135deg,#f0ece8,#cdbfb3)"></div>
  <ul class="bul tight abs" style="left:23px;top:153px;width:150px;font-size:7px"><li>Lorem ipsum dolor sit amet, consectetuer adipiscing elit. Maecenas porttitor congue massa.</li><li>habitant morbi tristique senectus et netus et malesuada fames ac turpis egestas. Proin pharetra nonummy pede. Mauris et orci.</li></ul>
  <ul class="bul tight abs" style="left:189px;top:153px;width:150px;font-size:7px"><li>Lorem ipsum dolor sit amet, consectetuer adipiscing elit. Maecenas porttitor congue massa.</li><li>habitant morbi tristique senectus et netus et malesuada fames ac turpis egestas. Proin pharetra nonummy pede. Mauris et orci.</li></ul>
  <ul class="bul tight abs" style="left:355px;top:153px;width:150px;font-size:7px"><li>Lorem ipsum dolor sit amet, consectetuer adipiscing elit. Maecenas porttitor congue massa.</li><li>habitant morbi tristique senectus et netus et malesuada fames ac turpis egestas. Proin pharetra nonummy pede. Mauris et orci.</li></ul>
  <div class="foot"><span class="pg">7</span><span class="copy">©2023 MOLVARO | ALL RIGHTS RESERVED</span><span class="brand">Molvaro</span></div>
</section>

<!-- 8 three icon columns -->
<section class="slide" style="left:593px;top:528px">
  <div class="strip"></div>
  <div class="s-title" style="left:0;width:100%;text-align:center">Slide title</div>
  <svg class="abs" style="left:0;top:55px" width="529" height="70" viewBox="0 0 529 70">
    <g fill="none" stroke-width="2.2">
      <g stroke="#1b57a3"><circle cx="98" cy="38" r="30"/><line x1="98" y1="68" x2="98" y2="83"/><line x1="60" y1="83" x2="136" y2="83"/>
        <path d="M92 22 h10 v22 h-10z M84 52 h28"/></g>
      <g stroke="#74bb1f"><circle cx="264" cy="38" r="30"/><line x1="264" y1="68" x2="264" y2="83"/><line x1="226" y1="83" x2="302" y2="83"/>
        <circle cx="264" cy="32" r="6"/><path d="M252 52 q12 -14 24 0"/></g>
      <g stroke="#e1262d"><circle cx="430" cy="38" r="30"/><line x1="430" y1="68" x2="430" y2="83"/><line x1="392" y1="83" x2="468" y2="83"/>
        <circle cx="423" cy="28" r="4"/><circle cx="437" cy="28" r="4"/><path d="M417 52 v-14 h12 v14 M431 52 v-14 h12 v14"/></g>
    </g>
  </svg>
  <div class="col3 t-blue" style="left:23px">Lorem ipsum dolor sit amet, consectetuer adipiscing elit. Maecenas porttitor congue massa. habitant morbi tristique senectus et netus et malesuada fames ac turpis egestas. Proin pharetra nonummy pede. Mauris et orci.</div>
  <div class="col3 t-green" style="left:189px">Lorem ipsum dolor sit amet, consectetuer adipiscing elit. Maecenas porttitor congue massa. habitant morbi tristique senectus et netus et malesuada fames ac turpis egestas. Proin pharetra nonummy pede. Mauris et orci.</div>
  <div class="col3 t-red" style="left:355px">Lorem ipsum dolor sit amet, consectetuer adipiscing elit. Maecenas porttitor congue massa. habitant morbi tristique senectus et netus et malesuada fames ac turpis egestas. Proin pharetra nonummy pede. Mauris et orci.</div>
  <div class="foot"><span class="pg">8</span><span class="copy">©2023 MOLVARO | ALL RIGHTS RESERVED</span><span class="brand">Molvaro</span></div>
</section>

<!-- 9 section breaker -->
<section class="slide" style="left:15px;top:696px">
  <div class="strip"></div>
  <div class="abs" style="left:0;top:30px;width:100%;text-align:center;font-family:'Rubik',sans-serif;font-weight:600;font-size:23px;color:var(--blue)">Section breaker</div>
  <div class="abs" style="left:0;top:60px;width:100%;text-align:center;font-family:'Rubik',sans-serif;font-weight:500;font-size:12px;color:var(--green)">Section descriptor</div>
  <div class="photo" role="img" aria-label="Foto: arts met stethoscoop" style="left:0;top:100px;width:529px;height:165px;background:linear-gradient(90deg,#dfe9f3,#e9eef2 40%,#c7d8ea 70%,#e3edf6)"></div>
  <div class="foot"><span class="pg">9</span><span class="copy">©2023 MOLVARO | ALL RIGHTS RESERVED</span><span class="brand">Molvaro</span></div>
</section>

<!-- 10 full photo -->
<section class="slide" style="left:304px;top:696px">
  <div class="photo" role="img" aria-label="Foto: bestralingsapparaat met patiënt" style="left:0;top:0;width:529px;height:297px;background:linear-gradient(120deg,#3b4fd1,#6e86e8 35%,#c8d2f3 50%,#5a6fd6 70%,#2b3aa6)"></div>
  <div class="hero-title" style="top:168px;font-size:25px">Chemo of bestraling</div>
  <div class="hero-text" style="top:200px;width:250px">Lorem ipsum dolor sit amet, consectetuer adipiscing elit. Maecenas porttitor congue massa. Fusce posuere, magna sed pulvinar ultricies, purus lectus malesuada</div>
</section>

<!-- 11 Risicofactoren -->
<section class="slide" style="left:593px;top:696px">
  <div class="strip"></div>
  <div class="s-title">Risicofactoren</div>
  <div class="bar blue" style="left:23px;top:65px;width:222px">DIABETES (MELLITUS)</div>
  <div class="bar green" style="left:284px;top:65px;width:222px">SJÖGREN</div>
  <div class="photo" role="img" aria-label="Foto: bloedsuikermeter en medicatie" style="left:23px;top:89px;width:222px;height:67px;background:linear-gradient(135deg,#8ec6e0,#cfe6f1 50%,#6fb1d3)"></div>
  <div class="photo" role="img" aria-label="Foto: boek over het syndroom van Sjögren" style="left:284px;top:89px;width:222px;height:67px;background:linear-gradient(135deg,#2b2b2b,#3b3a34 60%,#5a4a2a)"></div>
  <div class="abs t-blue" style="left:23px;top:160px;font-weight:600;font-size:9px">Type I of II</div>
  <ul class="bul tight abs" style="left:23px;top:173px;width:222px"><li>Snel bloedend tandvlees</li><li>Droge mond</li><li>Meer eetmomenten (ook in de nacht)</li><li>Koolhydraten en suikers</li><li>Stabiel of niet?</li><li>Gebruik Insuline?</li></ul>
  <div class="abs t-green" style="left:284px;top:160px;font-weight:600;font-size:9px">Vorm van reuma</div>
  <ul class="bul tight abs" style="left:284px;top:173px;width:222px"><li>Ontsteking aan speekselklieren</li><li>Droge mond</li><li>Meer plakvorming</li></ul>
  <div class="foot"><span class="pg">11</span><span class="copy">©2023 MOLVARO | ALL RIGHTS RESERVED</span><span class="brand">Molvaro</span></div>
</section>

<!-- 12 INR -->
<section class="slide" style="left:15px;top:863px">
  <div class="strip"></div>
  <div class="s-title">INR en</div>
  <div class="abs" style="left:23px;top:60px;font-family:'Rubik',sans-serif;font-weight:500;font-size:12px;color:var(--green)">stollingsfactorenpercentage</div>
  <div class="photo" role="img" aria-label="Foto: winkelwagentje met medicijnen" style="left:0;top:108px;width:247px;height:157px;background:linear-gradient(135deg,#cfe0ef,#a8c6e2 60%,#8fb3d8)"></div>
  <table class="inr">
    <tr><th>INR</th><th>Stollingspercentage</th></tr>
    <tr class="norm"><td>1.0</td><td>100</td></tr>
    <tr><td>1.2</td><td>50</td></tr>
    <tr><td>1.8</td><td>20</td></tr>
    <tr><td>2.5</td><td>12</td></tr>
    <tr><td>3.0</td><td>9</td></tr>
    <tr><td><b>meer dan 4.0</b></td><td><b>minder dan 5</b></td></tr>
  </table>
  <div class="inr-note">Een INR van 1.0-1.2 is normaal</div>
  <div class="foot"><span class="pg">12</span><span class="copy">©2023 MOLVARO | ALL RIGHTS RESERVED</span><span class="brand">Molvaro</span></div>
</section>

<!-- 13 Diabetes & medicatie -->
<section class="slide" style="left:304px;top:863px">
  <div class="strip"></div>
  <div class="s-title">Diabetes &amp; medicatie</div>
  <div class="bar blue" style="left:23px;top:65px;width:222px">TYPE I</div>
  <div class="bar green" style="left:284px;top:65px;width:222px">TYPE II</div>
  <ul class="bul tight abs" style="left:23px;top:91px;width:240px"><li>Auto-immuunziekte</li><li>Schommelende bloedsuikerwaarde</li><li>Altijd gebruik Insuline (Aspart, Glarex, Rapilin)</li><li>Droge mond, bloedende tandvlees</li><li>Meer eet- drink momenten (ook in de nacht)</li><li>Meer suikers nodig (koolhydraten)</li><li>Vaak ook schildklierafwijking</li></ul>
  <ul class="bul tight abs" style="left:284px;top:91px;width:222px"><li>Leefstijladvies</li><li>Tablet (metformine)</li><li>Enkele gevallen (tijdelijk) insuline</li><li>Smaakstoornis</li><li>Braken en misselijkheid (beginfase)</li></ul>
  <div class="photo" role="img" aria-label="Foto: suikerklontjes" style="left:0;top:198px;width:529px;height:67px;background:linear-gradient(90deg,#8a7454,#d8d2c6 30%,#f2f0ec 60%,#c9bda8)"></div>
  <div class="foot"><span class="pg">13</span><span class="copy">©2023 MOLVARO | ALL RIGHTS RESERVED</span><span class="brand">Molvaro</span></div>
</section>

<!-- 14 Dossiervoering -->
<section class="slide" style="left:593px;top:863px">
  <div class="strip"></div>
  <div class="s-title">Dossiervoering</div>
  <div class="abs" style="left:23px;top:60px;font-family:'Rubik',sans-serif;font-weight:500;font-size:12px;color:var(--green)">Vaste volgorde</div>
  <div class="photo" role="img" aria-label="Foto: hand met gekleurde capsules" style="left:262px;top:0;width:267px;height:267px;background:linear-gradient(135deg,#8a6a58,#3a3430 45%,#262626)"></div>
  <div class="abs" style="left:23px;top:92px;font-size:7.8px;font-weight:600">Begin vooraf met een check op:</div>
  <ul class="bul tight abs" style="left:23px;top:103px;width:230px;font-size:7.8px"><li>cariësactiviteit verleden</li><li>zorgplan</li><li>medische anamnese (Vraag goed door!)</li><li>wensen vragen of klachten van patiënt bekend?</li><li>reeds geplande afspraken</li><li>laatste bezoek tandarts en mondhygiënist/preventie</li><li>status preasens</li><li>BW's of solo's</li><li>wang/ slijmvliezen</li></ul>
  <div class="foot"><span class="pg">14</span><span class="copy">©2023 MOLVARO | ALL RIGHTS RESERVED</span><span class="brand">Molvaro</span></div>
</section>

<!-- 15 Dossiervoering two bars -->
<section class="slide" style="left:15px;top:1031px">
  <div class="strip"></div>
  <div class="s-title">Dossiervoering</div>
  <div class="bar blue" style="left:23px;top:65px;width:222px">TITLE</div>
  <div class="bar green" style="left:284px;top:65px;width:222px">TITLE</div>
  <ul class="bul tight abs" style="left:23px;top:89px;width:222px;font-size:6.8px"><li>PO uitgevoerd door/ in opdracht van</li><li>Med:</li><li>Wvk:</li><li>Paro/MH/Zelfzorg:</li><li>Röntgen:</li><li>Slijtage (attritie/erosie):</li><li>Gnatho/TMD:</li><li>Indicatie fluorid</li></ul>
  <ul class="bul tight abs" style="left:284px;top:89px;width:222px;font-size:6.8px"><li>PPS</li><li>ASA</li><li>Zorgplan (cariësrisico etc.)</li><li>NAW gegevens</li></ul>
  <div class="photo" role="img" aria-label="Foto: arts met stethoscoop" style="left:0;top:198px;width:529px;height:67px;background:linear-gradient(90deg,#dfe9f3,#e9eef2 40%,#c7d8ea 70%,#e3edf6)"></div>
  <div class="foot"><span class="pg">15</span><span class="copy">©2023 MOLVARO | ALL RIGHTS RESERVED</span><span class="brand">Molvaro</span></div>
</section>

<!-- 16 Protocol -->
<section class="slide" style="left:304px;top:1031px">
  <div class="strip"></div>
  <div class="s-title">Protocol &amp; follow up</div>
  <svg class="abs" style="left:0;top:60px" width="529" height="90" viewBox="0 0 529 90">
    <line x1="23" y1="84" x2="506" y2="84" stroke="#74bb1f" stroke-width="1"/>
    <g>
      <path d="M74 2 a32 32 0 0 1 32 32 c0 20 -32 44 -32 44 s-32 -24 -32 -44 a32 32 0 0 1 32 -32z" fill="#1b57a3"/><circle cx="74" cy="34" r="24" fill="#fff"/><circle cx="74" cy="84" r="3.5" fill="#1b57a3"/>
      <path d="M200 2 a32 32 0 0 1 32 32 c0 20 -32 44 -32 44 s-32 -24 -32 -44 a32 32 0 0 1 32 -32z" fill="#74bb1f"/><circle cx="200" cy="34" r="24" fill="#fff"/><circle cx="200" cy="84" r="3.5" fill="#74bb1f"/>
      <path d="M327 2 a32 32 0 0 1 32 32 c0 20 -32 44 -32 44 s-32 -24 -32 -44 a32 32 0 0 1 32 -32z" fill="#1b57a3"/><circle cx="327" cy="34" r="24" fill="#fff"/><circle cx="327" cy="84" r="3.5" fill="#1b57a3"/>
      <path d="M454 2 a32 32 0 0 1 32 32 c0 20 -32 44 -32 44 s-32 -24 -32 -44 a32 32 0 0 1 32 -32z" fill="#74bb1f"/><circle cx="454" cy="34" r="24" fill="#fff"/><circle cx="454" cy="84" r="3.5" fill="#74bb1f"/>
    </g>
    <g fill="none" stroke-width="2">
      <g stroke="#1b57a3"><circle cx="68" cy="28" r="4"/><circle cx="80" cy="28" r="4"/><path d="M62 46 v-10 h12 v10 M74 46 v-10 h12 v10"/></g>
      <g stroke="#74bb1f"><path d="M200 28 c-4 -6 -12 -2 -8 4 l8 8 l8 -8 c4 -6 -4 -10 -8 -4z"/><path d="M188 46 q12 -10 24 0"/></g>
      <g stroke="#1b57a3"><circle cx="327" cy="26" r="6"/><path d="M315 46 v-6 q12 -10 24 0 v6z"/></g>
      <g stroke="#74bb1f"><path d="M454 30 c-4 -6 -12 -2 -8 4 l8 8 l8 -8 c4 -6 -4 -10 -8 -4z"/><path d="M440 48 l14 -4 l14 4"/></g>
    </g>
  </svg>
  <div class="pin-lbl t-blue" style="left:24px">Waar loop je tegenaan?</div>
  <div class="pin-lbl t-green" style="left:150px">Wat heb jij nodig van je collega en team?<small>Geef dit op tijd aan</small></div>
  <div class="pin-lbl t-blue" style="left:277px">Maak een protocol<small>Evalueer regelmatig en bekijk eventuele aanpassingen</small></div>
  <div class="pin-lbl t-green" style="left:404px">Evaluatie (door) plannen<small>Licht kort toe wat je wilt bespreken.</small></div>
  <div class="foot"><span class="pg">16</span><span class="copy">©2023 MOLVARO | ALL RIGHTS RESERVED</span><span class="brand">Molvaro</span></div>
</section>

<!-- 17 Thank you -->
<section class="slide" style="left:593px;top:1031px">
  <div class="photo" role="img" aria-label="Foto: onderzoeker bij een microscoop, groen getint" style="left:0;top:0;width:529px;height:297px;background:linear-gradient(120deg,#5f9a5a,#7dae62 40%,#9cc07a 65%,#6e9e68)"></div>
  <div class="abs" style="left:25px;top:88px;font-family:'Rubik',sans-serif;font-weight:700;font-size:44px;line-height:.95;color:#fff">THANK<br>YOU!</div>
  <div class="abs" style="left:25px;top:188px;font-size:12px;color:#fff">Follow Molvaro on:</div>
  <svg class="abs" style="left:25px;top:208px" width="130" height="26" viewBox="0 0 130 26">
    <g fill="none" stroke="#fff" stroke-width="2.2"><circle cx="12" cy="13" r="10.5"/><circle cx="46" cy="13" r="10.5"/><circle cx="80" cy="13" r="10.5"/><circle cx="114" cy="13" r="10.5"/></g>
  </svg>
  <div class="abs" style="left:25px;top:248px;font-size:10px;color:#fff">www.molvaro.com</div>
</section>

</body>
</html>
```